Welcome Card for first time customers

This card is for LeafHarbor and will be included with the first purchase. We are an online company that deals with cannabis. We want to capture our first time buyers and turn them into life long customers. This card is aimed to show them all the benefits of being a returning a customer with us as well as thanking them for choosing us from our many competitors.

This card will be the same size as a postcard (4 x 6 inches) and needs to be double sided.

*if you need a different format for our logos just ask
**THE WINNER WILL BE ASKED TO COMPLETE FUTURE PROJECTS

Target Market(s)

19+

Industry/Entity Type

Cannabis

Requirements
Must have
• - Welcome phrase: "Welcome to the LHR family"

- space for discount code with second spot for the expiration date underneath. Phrase: "Save 15% off your next purchase"

- Perks of being a part of the family:

1. Loyalty Program "Once you've made 5 orders with us you'll be able to join our Loyalty Program! You’ll receive 2.5% back in points with every order to use towards a future purchase. So go ahead, indulge. You deserve it!"

2. Referral Program "Refer a friend using your customer number and they will receive $25 off their first purchase with us AND you'll also receive $25 for your next purchase! Get the full details and customer number at https://www.leafharbor-shop.example/loyalty/"

- Contact information: Website: leafharbor-shop.example. Phone number: 1-833-555-LEAF. Instagram: leafharbor_nth
Nice to have
• Graphic photo side of the postcard to have a design that really stands out, looking modern and sophisticated with a good use of space and colour. Would love to see use of lifestyle cannabis images or real life images. inspirational photos are attached. Include the welcome phrase on this side.

Text side of postcard to use the space well while including the 2 perks.

```html
<!DOCTYPE html>
<html lang="en">
<head>
<meta charset="utf-8">
<title>LeafHarbor Welcome Card</title>
<link rel="stylesheet" href="https://fonts.googleapis.com/css2?family=Montserrat:wght@400;700;800&family=Mulish:wght@400;700&family=Kaushan+Script&display=swap">
<style>
  :root {
    --stage: #a4a4a4;
    --label: #e6e6e6;
    --green: #7cc242;
    --green-dark: #5fa22c;
    --ink: #1f1f1f;
    --ink-soft: #2b2b2b;
    --paper: #fbfbfb;
    --edge: #e4e4e4;
    --code-line: #9a9a9a;
    --code-text: #d8d8d8;
    --footer: #1e1e1e;
    --footer-text: #ffffff;
  }
  * { box-sizing: border-box; margin: 0; padding: 0; }
  html, body { width: 1200px; height: 600px; overflow: hidden; }
  body {
    background: var(--stage);
    font-family: "Mulish", sans-serif;
    position: relative;
  }
  .panel-label {
    position: absolute;
    top: 24px;
    font-family: "Montserrat", sans-serif;
    font-weight: 400;
    font-size: 17px;
    color: var(--label);
  }
  .card {
    position: absolute;
    top: 56px;
    width: 353px;
    height: 493px;
    background: var(--paper);
    overflow: hidden;
    text-align: center;
    color: var(--ink);
  }
  .card--sample-one { left: 34px; border: 7px solid var(--edge); border-bottom: 0; }
  .card--sample-two { left: 429px; border: 7px solid var(--green); border-bottom: 0; }
  .card--back { left: 819px; top: 54px; height: 495px; border: 7px solid var(--edge); border-right-color: var(--green); border-bottom: 0; }

  .card__inner { position: absolute; inset: -7px -7px 0 -7px; }

  .brand {
    position: absolute;
    left: 0; right: 0;
    display: flex; align-items: center; justify-content: center; gap: 7px;
    font-family: "Montserrat", sans-serif;
    font-weight: 800;
    color: var(--ink);
  }
  .brand__mark { width: 14px; height: 14px; background: var(--green); flex: none; }
  .brand--front { top: 52px; font-size: 24px; }
  .brand-block {
    position: absolute; left: 115px; top: 0; width: 123px; height: 118px;
    background: var(--ink);
    display: flex; align-items: center; justify-content: center; gap: 5px;
    font-family: "Montserrat", sans-serif; font-weight: 800; font-size: 14px;
    color: var(--footer-text);
  }
  .brand-block .brand__mark { width: 10px; height: 10px; }
  .brand--back { top: 32px; font-size: 15px; gap: 5px; }
  .brand--back .brand__mark { width: 10px; height: 10px; }

  .welcome {
    position: absolute; left: 0; right: 0;
    font-family: "Montserrat", sans-serif; font-weight: 400;
    font-size: 24px; line-height: 1;
  }
  .welcome__family {
    position: absolute; left: 0; right: 0;
    font-family: "Montserrat", sans-serif; font-weight: 800;
    font-size: 48px; line-height: 1; color: var(--green);
  }
  .card--sample-one .welcome { top: 122px; }
  .card--sample-one .welcome__family { top: 143px; }
  .card--sample-two .welcome { top: 127px; }
  .card--sample-two .welcome__family { top: 147px; }

  .offer {
    position: absolute; left: 0; right: 0; top: 199px;
    font-family: "Montserrat", sans-serif; font-weight: 700;
    font-size: 8.6px; line-height: 1; color: var(--ink);
  }
  .discount-code {
    position: absolute; left: 70px; top: 211px; width: 212px; height: 32px;
    border: 1.5px dashed var(--code-line); border-radius: 6px;
    font-family: "Montserrat", sans-serif; font-weight: 700;
    font-size: 18px; line-height: 29px; color: var(--code-text);
  }
  .expiry {
    position: absolute; left: 121px; top: 247px; width: 110px; height: 15px;
    border: 1px dashed var(--code-line); border-radius: 4px;
    font-family: "Montserrat", sans-serif; font-weight: 700;
    font-size: 7.5px; line-height: 13px; color: #c4c4c4;
  }
  .tagline {
    position: absolute; left: 0; right: 0; top: 264px;
    display: flex; justify-content: center; align-items: center; gap: 6px;
    font-family: "Kaushan Script", cursive; font-size: 17px; line-height: 1; color: var(--ink);
  }
  .tagline__badge {
    width: 19px; height: 19px; border-radius: 50%; background: #f7c534;
  }
  .tagline__underline {
    position: absolute; left: 178px; top: 289px; width: 78px; height: 2px;
    background: var(--green); border-radius: 2px;
  }
  .tagline__dot {
    position: absolute; left: 261px; top: 289px; width: 4px; height: 3px;
    background: var(--green); border-radius: 50%;
  }

  .perk {
    position: absolute; left: 26px; right: 26px;
    font-size: 7.4px; line-height: 9.4px; color: var(--ink-soft);
  }
  .perk__title { color: var(--green); font-weight: 700; }
  .perk strong { font-weight: 700; }
  .perk--loyalty { top: 302px; }
  .perk--referral { top: 338px; }
  .perk-details {
    position: absolute; left: 0; right: 0; top: 366px;
    font-size: 8.4px; font-weight: 700; color: var(--ink);
  }
  .loyalty-link {
    position: absolute; left: 84px; top: 381px; width: 185px; height: 21px;
    background: linear-gradient(var(--green), var(--green-dark));
    border-radius: 11px; box-shadow: 0 0 0 2px #fff, 0 1px 4px rgba(0,0,0,.35);
    font-size: 6.6px; font-weight: 700; line-height: 21px; color: var(--footer-text);
    white-space: nowrap;
    z-index: 2;
  }

  .footer-wave { position: absolute; left: 0; bottom: 0; width: 353px; height: 120px; }

  .contact {
    position: absolute; left: 0; right: 0; bottom: 0; height: 70px;
    color: var(--footer-text);
  }
  .contact__icon { position: absolute; left: 15px; top: 17px; width: 42px; height: 36px; }
  .contact__phone {
    position: absolute; left: 62px; top: 13px; width: 198px; text-align: center;
    font-family: "Montserrat", sans-serif; font-weight: 700; font-size: 22px; line-height: 1;
    white-space: nowrap;
  }
  .contact__site {
    position: absolute; left: 62px; top: 40px; width: 198px; text-align: center;
    font-family: "Montserrat", sans-serif; font-size: 7.6px; white-space: nowrap;
  }
  .contact__site b { font-weight: 700; }
  .contact__divider { position: absolute; left: 264px; top: 12px; width: 1px; height: 42px; background: #777; }
  .contact__social {
    position: absolute; left: 266px; right: 0; top: 14px;
    display: flex; flex-direction: column; align-items: center; gap: 6px;
    font-family: "Montserrat", sans-serif; font-weight: 700; font-size: 8.4px;
  }
  .contact__social-mark { width: 17px; height: 17px; border: 2px solid var(--green); border-radius: 50%; }

  .back-headline {
    position: absolute; left: 0; right: 0; top: 88px;
    font-family: "Montserrat", sans-serif; font-weight: 800;
    font-size: 33px; line-height: 35px; color: var(--green);
  }
  .back-intro {
    position: absolute; left: 0; right: 0; top: 160px;
    font-size: 9px; line-height: 13px; color: var(--ink);
  }
  .lifestyle-photo {
    position: absolute; left: 0; right: 0; top: 190px; height: 240px;
    background: linear-gradient(180deg, var(--paper) 0%, #ecdfe6 22%, #d8c2c6 45%, #c2a184 68%, #8a6a4c 88%, #5e4634 100%);
  }
</style>
</head>
<body>

  <div class="panel-label" style="left:32px">Sample 1</div>
  <div class="panel-label" style="left:429px">Sample 2</div>
  <div class="panel-label" style="left:818px; font-size:22px; top:20px">BACK</div>

  <section class="card card--sample-one">
    <div class="card__inner">
      <div class="brand brand--front"><span class="brand__mark"></span>LeafHarbor</div>
      <div class="welcome">Welcome to the</div>
      <div class="welcome__family">LHR FAMILY</div>
      <div class="offer">Save 15% off your next purchase</div>
      <div class="discount-code">Discount Code</div>
      <div class="expiry">Expiration Date</div>
      <div class="tagline">For when you run out <span class="tagline__badge" role="img" aria-label="Winking emoji"></span></div>
      <div class="tagline__underline"></div><div class="tagline__dot"></div>
      <p class="perk perk--loyalty"><span class="perk__title">Loyalty Program</span> - Once you've made 5 orders with us you'll be able to join our Loyalty Program! <strong>You’ll receive 2.5%</strong> back in points with every order to use towards a future purchase. So go ahead, indulge. You deserve it!</p>
      <p class="perk perk--referral"><span class="perk__title">Referral Program</span> &nbsp;- &nbsp;Refer a friend using your customer number and they will receive $25 off their first purchase with us AND you'll also receive $25 for your next purchase!</p>
      <p class="perk-details">Get the full details and customer number at</p>
      <div class="loyalty-link">https://www.leafharbor-shop.example/loyalty/</div>
      <svg class="footer-wave" viewBox="0 0 353 120" preserveAspectRatio="none">
        <path d="M0,2 Q170,78 353,10 L353,22 Q176,92 0,18 Z" fill="var(--green)"/>
        <path d="M0,18 Q176,92 353,22 L353,36 Q176,104 0,32 Z" fill="#e0e0e0"/>
        <path d="M0,28 Q176,104 353,32 L353,120 L0,120 Z" fill="var(--footer)"/>
      </svg>
      <div class="contact">
        <svg class="contact__icon" viewBox="0 0 42 36" fill="none" stroke="var(--green)" stroke-width="2.4" stroke-linejoin="round">
          <path d="M2,2 H28 V20 H10 L4,26 V20 H2 Z"/>
          <path d="M6,8 H24 M6,14 H18"/>
          <path d="M16,14 H40 V30 H36 V35 L31,30 H16 Z" fill="var(--footer)"/>
          <circle cx="23" cy="22" r="1" fill="var(--green)"/><circle cx="28" cy="22" r="1" fill="var(--green)"/><circle cx="33" cy="22" r="1" fill="var(--green)"/>
        </svg>
        <div class="contact__phone">1-833-555-LEAF</div>
        <div class="contact__site">Visit us at : <b>www.leafharbor-shop.example</b></div>
        <div class="contact__divider"></div>
        <div class="contact__social"><span class="contact__social-mark"></span>leafharbor_nth</div>
      </div>
    </div>
  </section>

  <section class="card card--sample-two">
    <div class="card__inner">
      <div class="brand-block"><span class="brand__mark"></span>LeafHarbor</div>
      <div class="welcome">Welcome to the</div>
      <div class="welcome__family">LHR FAMILY</div>
      <div class="offer">Save 15% off your next purchase</div>
      <div class="discount-code">Discount Code</div>
      <div class="expiry">Expiration Date</div>
      <div class="tagline">For when you run out <span class="tagline__badge" role="img" aria-label="Winking emoji"></span></div>
      <div class="tagline__underline"></div><div class="tagline__dot"></div>
      <p class="perk perk--loyalty"><span class="perk__title">Loyalty Program</span> - Once you've made 5 orders with us you'll be able to join our Loyalty Program! <strong>You’ll receive 2.5%</strong> back in points with every order to use towards a future purchase. So go ahead, indulge. You deserve it!</p>
      <p class="perk perk--referral"><span class="perk__title">Referral Program</span> &nbsp;- &nbsp;Refer a friend using your customer number and they will receive $25 off their first purchase with us AND you'll also receive $25 for your next purchase!</p>
      <p class="perk-details">Get the full details and customer number at</p>
      <div class="loyalty-link">https://www.leafharbor-shop.example/loyalty/</div>
      <svg class="footer-wave" viewBox="0 0 353 120" preserveAspectRatio="none">
        <path d="M0,2 Q170,78 353,10 L353,22 Q176,92 0,18 Z" fill="var(--green)"/>
        <path d="M0,18 Q176,92 353,22 L353,36 Q176,104 0,32 Z" fill="#e0e0e0"/>
        <path d="M0,28 Q176,104 353,32 L353,120 L0,120 Z" fill="var(--footer)"/>
      </svg>
      <div class="contact">
        <svg class="contact__icon" viewBox="0 0 42 36" fill="none" stroke="var(--green)" stroke-width="2.4" stroke-linejoin="round">
          <path d="M2,2 H28 V20 H10 L4,26 V20 H2 Z"/>
          <path d="M6,8 H24 M6,14 H18"/>
          <path d="M16,14 H40 V30 H36 V35 L31,30 H16 Z" fill="var(--footer)"/>
          <circle cx="23" cy="22" r="1" fill="var(--green)"/><circle cx="28" cy="22" r="1" fill="var(--green)"/><circle cx="33" cy="22" r="1" fill="var(--green)"/>
        </svg>
        <div class="contact__phone">1-833-555-LEAF</div>
        <div class="contact__site">Visit us at : <b>www.leafharbor-shop.example</b></div>
        <div class="contact__divider"></div>
        <div class="contact__social"><span class="contact__social-mark"></span>leafharbor_nth</div>
      </div>
    </div>
  </section>

  <section class="card card--back">
    <div class="card__inner">
      <div class="lifestyle-photo" role="img" aria-label="Lifestyle photo of a group of friends embracing, seen from behind, at sunset over hills"></div>
      <div class="brand brand--back"><span class="brand__mark"></span>LeafHarbor</div>
      <h1 class="back-headline">LEAF HARBOR.<br>SIMPLE.</h1>
      <p class="back-intro">All your cannabis needs at great prices from LeafHarbor.<br>Go Ahead, Take a look around our shop.</p>
      <svg class="footer-wave" viewBox="0 0 353 120" preserveAspectRatio="none">
        <path d="M0,2 Q170,78 353,10 L353,22 Q176,92 0,18 Z" fill="var(--green)"/>
        <path d="M0,18 Q176,92 353,22 L353,36 Q176,104 0,32 Z" fill="#e0e0e0"/>
        <path d="M0,28 Q176,104 353,32 L353,120 L0,120 Z" fill="var(--footer)"/>
      </svg>
      <div class="contact">
        <svg class="contact__icon" viewBox="0 0 42 36" fill="none" stroke="var(--green)" stroke-width="2.4" stroke-linejoin="round">
          <path d="M2,2 H28 V20 H10 L4,26 V20 H2 Z"/>
          <path d="M6,8 H24 M6,14 H18"/>
          <path d="M16,14 H40 V30 H36 V35 L31,30 H16 Z" fill="var(--footer)"/>
          <circle cx="23" cy="22" r="1" fill="var(--green)"/><circle cx="28" cy="22" r="1" fill="var(--green)"/><circle cx="33" cy="22" r="1" fill="var(--green)"/>
        </svg>
        <div class="contact__phone">1-833-555-LEAF</div>
        <div class="contact__site">Visit us at : <b>www.leafharbor-shop.example</b></div>
        <div class="contact__divider"></div>
        <div class="contact__social"><span class="contact__social-mark"></span>leafharbor_nth</div>
      </div>
    </div>
  </section>

</body>
</html>
```